8" x 11" One Page Flyer for Fence Installation Company

We are looking to promote our business with a new flyer that would be handed out in person to people or put at their mailbox/door at their homes. The flyer needs to be creative and attention-grabbing. I have attached some of our previous flyers and our website information. Do not call or email regarding the flyer. We want the flyer to look professional but also friendly. One page, NOT folded. You can use images from our website at www.MyBraxtonYard.com or our online page at www.Facebook.com/HollowbrookRailsBKT. We are flexible with what photos you can use but there must be photos of OUR fences on the flyer. More photos specifically can also be provided. Colors need to be suitable for a flyer printed on canary yellow in color paper OR white paper.

Target Market(s)

Homeowners that need a new fence

Industry/Entity Type

Construction

Font styles to use
Sans Serif
Other font styles liked:
• HD Colton

Colors
0054AA
0677BA
7BADD7
CADEEF
E8F1F8
0094D4
00A9DD
6FCCEA
C7EBF8
E9F6FB

Requirements
Must have
• Our fence photos - mostly wood fence photos (different designs), SIZE SHOULD BE LETTER SIZE 8" x 11"
Nice to have
• A nice bible verse featured at the bottom of the flyer.
Should not have
• DO NOT COPY THE WEBSITE FORMAT, I WANT SOMETHING UNIQUE. Other people's fence photos, they must all come from our website or facebook page

```html
<!DOCTYPE html>
<html lang="en">
<head>
<meta charset="utf-8">
<title>Hollowbrook Rails – We Build Fencing You Can Trust</title>
<link href="https://fonts.googleapis.com/css2?family=Poppins:wght@500;600;700;800&family=Montserrat:wght@500;700&display=swap" rel="stylesheet">
<style>
  :root {
    --sky: #0aa8dd;
    --navy: #253f8f;
    --royal: #2548a0;
    --light-blue: #6fcde9;
    --pale: #d8ebf1;
    --white: #ffffff;
    --ink: #1f1f1f;
    --brown: #8a4a2a;
    --photo-shadow: rgba(20, 60, 100, 0.18);
  }
  * { box-sizing: border-box; margin: 0; padding: 0; }
  html, body { width: 927px; height: 1200px; overflow: hidden; background: var(--white); }
  .flyer {
    position: relative;
    width: 927px;
    height: 1200px;
    overflow: hidden;
    background: var(--pale);
    font-family: "Poppins", sans-serif;
  }
  .hero-band {
    position: absolute; inset: 0 0 auto 0; height: 850px;
    background: var(--sky);
  }
  .hero-band svg { position: absolute; left: 0; top: 0; }
  .picket-row { position: absolute; background: rgba(255,255,255,0.85); }
  .picket-row.top-left { left: 0; top: 348px; width: 95px; height: 95px; opacity: .9; }
  .picket-row.top-right { left: 833px; top: 318px; width: 94px; height: 95px; opacity: .9; }
  .picket-row.bottom-left { left: 0; top: 862px; width: 95px; height: 70px; background: rgba(255,255,255,.55); }
  .picket-row.bottom-right { left: 833px; top: 828px; width: 94px; height: 70px; background: rgba(255,255,255,.55); }

  .headline {
    position: absolute; left: 64px; top: 90px;
    font-weight: 800; font-size: 94px; line-height: 1;
    letter-spacing: -2px; color: var(--navy);
    transform: rotate(-2deg); transform-origin: left center;
    white-space: nowrap;
  }
  .trust-tag {
    position: absolute; left: 386px; top: 167px;
    transform: rotate(-3deg);
  }
  .trust-tag .shadow {
    position: absolute; left: 11px; top: 11px; width: 404px; height: 78px;
    background: var(--light-blue);
  }
  .trust-tag .box {
    position: relative; width: 404px; height: 78px;
    background: var(--navy);
    display: flex; align-items: center; justify-content: center;
    font-weight: 700; font-size: 49px; letter-spacing: -.5px;
  }
  .trust-tag .soft { color: var(--light-blue); margin-right: 14px; }
  .trust-tag .strong { color: var(--white); }

  .gallery {
    position: absolute; left: 95px; top: 300px;
    display: grid;
    grid-template-columns: repeat(3, 234px);
    grid-template-rows: repeat(3, 203px);
    gap: 19px 19px;
  }
  .photo {
    border: 6px solid var(--white);
    border-radius: 14px;
    box-shadow: 0 4px 10px var(--photo-shadow);
  }
  .photo.wood { background: linear-gradient(160deg, #c9a877, #a88a5a 60%, #6d7f45); }
  .photo.picket { background: linear-gradient(160deg, #cfd3d6, #d9b97e 45%, #7b6e4a); }
  .photo.rail { background: linear-gradient(160deg, #5f7a3e, #c29a5c 50%, #6a4f33); }
  .photo.vinyl-rail { background: linear-gradient(170deg, #9bb0a4, #eef0ee 45%, #5f7a3a); }
  .photo.iron { background: linear-gradient(170deg, #d8e6ef, #3f5a32 50%, #5f8a3a); }
  .photo.vinyl-privacy { background: linear-gradient(170deg, #4d6a35, #f1f2f0 35%, #e6e8e6 70%, #6a5a3a); }
  .photo.scallop { background: linear-gradient(160deg, #9fb3c4, #d6b07a 45%, #9c7c4c); }
  .photo.gate { background: linear-gradient(160deg, #c8d8e3, #c7b998 40%, #8d7b5a); }
  .photo.arched { background: linear-gradient(160deg, #9a4f3d, #cdb27c 45%, #7f6a3e); }

  .contact {
    position: absolute; left: 0; width: 927px; top: 976px;
    text-align: center; color: var(--royal);
    font-weight: 700; font-size: 24.5px; letter-spacing: .5px; line-height: 36px;
    white-space: nowrap;
  }
  .contact .divider { margin: 0 12px; }
  .contact .social { display: inline-flex; align-items: center; gap: 12px; }
  .contact .dot {
    display: inline-block; width: 27px; height: 27px; border-radius: 50%;
    background: var(--royal);
  }

  .verse-mark { position: absolute; left: 51px; top: 1083px; }
  .verse {
    position: absolute; left: 161px; top: 1084px; width: 398px;
    font-family: "Montserrat", sans-serif; color: var(--royal);
    font-weight: 500; font-size: 16.8px; line-height: 20px;
  }
  .verse cite {
    display: block; margin-top: 6px;
    font-style: normal; font-weight: 700; font-size: 15.5px;
  }

  .brand-card {
    position: absolute; left: 655px; top: 1087px; width: 272px; height: 113px;
    background: var(--white); border-radius: 16px 0 0 0;
    display: flex; align-items: center; gap: 10px; padding-left: 34px;
  }
  .brand-card .mark { width: 42px; height: 42px; background: var(--brown); flex: none; }
  .brand-card .name { font-weight: 600; font-size: 16px; color: var(--sky); line-height: 1.15; white-space: nowrap; }
  .brand-card .phone { font-weight: 800; font-size: 16px; color: var(--ink); line-height: 1.25; }
  .brand-card .tagline { font-size: 5px; font-weight: 600; color: var(--ink); white-space: nowrap; }
</style>
</head>
<body>
<main class="flyer">
  <div class="hero-band">
    <svg width="927" height="260" viewBox="0 0 927 260" aria-hidden="true">
      <polygon points="0,73 927,33 927,211 0,251" fill="#ffffff"/>
    </svg>
  </div>

  <div class="picket-row top-left" role="img" aria-label="White picket fence illustration"></div>
  <div class="picket-row top-right" role="img" aria-label="White picket fence illustration"></div>
  <div class="picket-row bottom-left" role="img" aria-label="Faint picket fence illustration"></div>
  <div class="picket-row bottom-right" role="img" aria-label="Faint picket fence illustration"></div>

  <h1 class="headline">We Build Fencing</h1>
  <div class="trust-tag">
    <div class="shadow"></div>
    <div class="box"><span class="soft">You Can</span><span class="strong">Trust!</span></div>
  </div>

  <section class="gallery">
    <div class="photo wood" role="img" aria-label="Tall wooden privacy fence beside a flower bed"></div>
    <div class="photo picket" role="img" aria-label="Wooden picket fence with pointed tops along a house"></div>
    <div class="photo rail" role="img" aria-label="Wooden split rail fence with wire mesh"></div>
    <div class="photo vinyl-rail" role="img" aria-label="White three-rail vinyl fence across a lawn"></div>
    <div class="photo iron" role="img" aria-label="Black aluminum picket fence on green grass"></div>
    <div class="photo vinyl-privacy" role="img" aria-label="White vinyl privacy fence with lattice top"></div>
    <div class="photo scallop" role="img" aria-label="Wooden privacy fence with scalloped tops"></div>
    <div class="photo gate" role="img" aria-label="Arched wooden double gate with black hinges"></div>
    <div class="photo arched" role="img" aria-label="Arched wooden picket gate beside a brick house"></div>
  </section>

  <div class="contact">
    <div>Contact Us: 555 014 2736<span class="divider">|</span>www.mybraxtonyard.com</div>
    <div class="social"><span class="dot"></span>Follow us online! @ HollowbrookRailsBKT</div>
  </div>

  <svg class="verse-mark" width="90" height="66" viewBox="0 0 90 66" aria-hidden="true">
    <g fill="#0aa8dd">
      <path d="M4 40 C4 18 14 6 34 2 L36 12 C26 16 22 22 22 30 L38 30 L38 64 L4 64 Z"/>
      <path d="M50 40 C50 18 60 6 80 2 L82 12 C72 16 68 22 68 30 L84 30 L84 64 L50 64 Z"/>
    </g>
  </svg>
  <blockquote class="verse">
    In the day that thy walls are to be built, in that day shall the decree be far removed.
    <cite>MICAH 7:11</cite>
  </blockquote>

  <div class="brand-card">
    <span class="mark"></span>
    <div>
      <div class="name">Hollowbrook Rails</div>
      <div class="phone">555-014-2736</div>
      <div class="tagline">"Because Good Fences Make Good Neighbors"</div>
    </div>
  </div>
</main>
</body>
</html>
```